Nurturing Victors 6x9 book soft cover- front cover only

We need a book cover for a softcover book. We will need final files in Photoshop or InDesign is preferred.

Overall Title:
Nurturing Victors
Subtitle:
The Foundations of Humble Mentoring for Trainers, Instructors and Players
Author:
by Dr. Martin Hollis

The audience is high school and college coaches however we don't want the standard picture with words over the top. Make it a creative design but keep it mind it's a little academic.

```html
<!DOCTYPE html>
<html lang="en">
<head>
<meta charset="utf-8">
<title>Nurturing Victors — Book Cover</title>
<link rel="stylesheet" href="https://fonts.googleapis.com/css2?family=Questrial&display=swap">
<style>
  :root {
    --paper: #ffffff;
    --ink: #000000;
    --navy: #000c99;
    --red: #ff0000;
    --gold: #ffcc00;
    --frame: #f9c95a;
    --blue: #3737d6;
    --white: #ffffff;
    --crowd-grey: #8a8a8a;
  }
  * { margin: 0; padding: 0; box-sizing: border-box; }
  html, body { width: 800px; height: 1200px; overflow: hidden; background: var(--paper); }
  .cover {
    position: relative;
    width: 800px;
    height: 1200px;
    background: var(--paper);
    font-family: "Questrial", "Century Gothic", sans-serif;
    overflow: hidden;
  }
  .title-frame {
    position: absolute;
    left: 49px; top: 114px;
    width: 704px; height: 417px;
    border: 3px solid var(--frame);
  }
  .frame-star { position: absolute; top: 305px; width: 22px; height: 22px; }
  .frame-star--left { left: 40px; }
  .frame-star--right { left: 740px; }
  .title-kicker {
    position: absolute;
    top: 82px; left: 0; width: 800px;
    text-align: center;
    color: var(--navy);
    font-size: 70px;
    line-height: 1;
    letter-spacing: -2px;
    background: linear-gradient(var(--paper), var(--paper)) center / 460px 100% no-repeat;
  }
  .title-main {
    position: absolute;
    left: 0; width: 800px;
    text-align: center;
    color: var(--red);
    font-size: 212px;
    line-height: 1;
    letter-spacing: -4px;
  }
  .title-main--first { top: 168px; }
  .title-main--second { top: 330px; }
  .crowd-scene {
    position: absolute;
    left: 0; top: 520px;
    width: 800px; height: 300px;
    background: linear-gradient(to bottom, var(--paper) 0%, #c9c9c9 22%, var(--crowd-grey) 45%, var(--ink) 80%);
  }
  .lower-band {
    position: absolute;
    left: 0; top: 818px;
    width: 800px; height: 382px;
    background: var(--ink);
  }
  .subtitle {
    position: absolute;
    left: 69px; top: 845px;
    font-size: 34px;
    line-height: 43px;
    text-transform: uppercase;
    color: var(--white);
    letter-spacing: -0.5px;
  }
  .subtitle .accent-blue { color: var(--blue); }
  .subtitle .accent-gold { color: var(--gold); }
  .author {
    position: absolute;
    left: 0; top: 1120px;
    width: 800px;
    text-align: center;
    color: var(--white);
    font-size: 42px;
    letter-spacing: -0.5px;
  }
</style>
</head>
<body>
<main class="cover">
  <div class="crowd-scene" role="img" aria-label="Silhouette of a cheering crowd with a figure raising a gold trophy"></div>
  <div class="lower-band"></div>

  <div class="title-frame"></div>
  <svg class="frame-star frame-star--left" viewBox="0 0 24 24" aria-hidden="true"><polygon points="12,1 15,9 23,9 16.5,14 19,22 12,17 5,22 7.5,14 1,9 9,9" fill="#ffcc00"/></svg>
  <svg class="frame-star frame-star--right" viewBox="0 0 24 24" aria-hidden="true"><polygon points="12,1 15,9 23,9 16.5,14 19,22 12,17 5,22 7.5,14 1,9 9,9" fill="#ffcc00"/></svg>

  <h1>
    <span class="title-kicker">NURTURING</span>
    <span class="title-main title-main--first">VIC</span>
    <span class="title-main title-main--second">TORS</span>
  </h1>

  <p class="subtitle">
    The Foundations of<br>
    <span class="accent-blue">Humble Mentoring</span><br>
    For <span class="accent-gold">Trainers,</span><br>
    <span class="accent-gold">Instructors and Players</span>
  </p>

  <p class="author">DR. MARTIN HOLLIS</p>
</main>
</body>
</html>
```